Chat Software Business Card Design

We need a business card design for our company.

We provide businesses with a platform to communicate with their web visitors in real time using chat boxes on their web sites.

We're using a bright color scheme to attract attention on the site and the business card would do well to reflect this also to maintain brand awareness. However it is not essential to the ultimate design to use the same color scheme or feel as the site.

We offer a Free Trial of the software and would encourage a business card design to promote this if possible.

http://qelmarworks7.co.uk/projects/guest/index2.html

You will find the company logo attached also.

An eye catching design with something that will set the card apart from others is required.

The design of the card/theme of the card should be very unique, setting our selves apart, eye catching whilst not providing a "wacky" image for the company.

It should also include our contact information;~
Website - www.talkpond-live.com
Email - support@talkpond-live.com
Twitter - @Talkpondlive

Industry/Entity Type

Software

Contact Information for Business Card

Web - www.talkpond-live.com
Email - office@talkpond-live.com
Skype - Talkpond.Live

Requirements
Must have
• Use of company logo is required.

```html
<!DOCTYPE html>
<html lang="en">
<head>
<meta charset="utf-8">
<title>Talkpond.Live – Business Card</title>
<link rel="stylesheet" href="https://fonts.googleapis.com/css2?family=Source+Sans+3:wght@400;700&display=swap">
<style>
  :root {
    --orange-light: #fdb54a;
    --orange-mid: #fca033;
    --orange-edge: #ff7f00;
    --purple: #7f00ff;
    --white: #ffffff;
    --font: "Source Sans 3", "Myriad Pro", Arial, sans-serif;
  }
  html, body {
    margin: 0;
    padding: 0;
    overflow: hidden;
    background: var(--orange-edge);
  }
  .card {
    position: relative;
    width: 1200px;
    height: 741px;
    overflow: hidden;
    font-family: var(--font);
    background: radial-gradient(ellipse 70% 70% at 50% 50%, var(--orange-light) 0%, var(--orange-mid) 55%, var(--orange-edge) 100%);
  }
  .headline {
    position: absolute;
    top: 78px;
    left: 0;
    width: 1200px;
    margin: 0;
    text-align: center;
    color: var(--white);
    font-size: 45px;
    font-weight: 700;
    letter-spacing: 0.2px;
  }
  .contact {
    position: absolute;
    top: 192px;
    left: 0;
    margin: 0;
    display: grid;
    grid-template-columns: 391px auto;
    column-gap: 52px;
    row-gap: 4px;
    font-size: 50px;
    line-height: 61px;
  }
  .contact dt {
    text-align: right;
    color: var(--purple);
    font-weight: 700;
  }
  .contact dd {
    margin: 0;
    color: var(--white);
    font-weight: 400;
  }
  .features {
    position: absolute;
    inset: 0;
  }
  .feature-label {
    position: absolute;
    top: 608px;
    transform: translateX(-50%);
    color: var(--white);
    font-size: 31px;
    font-weight: 700;
    line-height: 36px;
    text-align: center;
    white-space: nowrap;
  }
  .feature-label.chat { left: 190px; }
  .feature-label.stats { left: 537px; }
  .feature-label.realtime { left: 955px; }
</style>
</head>
<body>
<main class="card">
  <h1 class="headline">Get more buyers through your website!</h1>

  <dl class="contact">
    <dt>Website:</dt><dd>www.talkpond-live.com</dd>
    <dt>Email:</dt><dd>support@talkpond-live.com</dd>
    <dt>Twitter:</dt><dd>@Talkpondlive</dd>
  </dl>

  <div class="features">
    <svg width="1200" height="741" viewBox="0 0 1200 741" aria-hidden="true">
      <defs>
        <radialGradient id="card-bg" gradientUnits="userSpaceOnUse" cx="600" cy="370" r="600" gradientTransform="translate(0 0) scale(1 0.62) translate(0 227)">
          <stop offset="0" stop-color="#fdb54a"/>
          <stop offset="0.55" stop-color="#fca033"/>
          <stop offset="1" stop-color="#ff7f00"/>
        </radialGradient>
      </defs>
      <g fill="none" stroke="#7f00ff" stroke-width="10" stroke-linejoin="round">
        <!-- chat boxes -->
        <path class="bubble-back" d="M112 464 H236 Q246 464 246 474 V563 Q246 573 236 573 H150 L126 592 V573 H112 Q102 573 102 563 V474 Q102 464 112 464 Z"/>
        <path class="bubble-front" fill="url(#card-bg)" d="M193 515 H279 Q289 515 289 525 V577 Q289 587 279 587 H215 L194 604 V587 H193 Q183 587 183 577 V525 Q183 515 193 515 Z"/>

        <!-- statistics monitor -->
        <rect class="monitor" x="473" y="464" width="144" height="102" rx="10"/>
        <polyline class="chart-line" points="503,532 540,503 565,521 589,499" stroke-width="6"/>

        <!-- laptop -->
        <rect class="laptop-screen" x="882" y="464" width="138" height="102" rx="10"/>
      </g>
      <g fill="#7f00ff">
        <polygon class="monitor-stand" points="525,571 565,571 580,592 510,592"/>
        <circle cx="503" cy="532" r="7"/>
        <circle cx="540" cy="503" r="7"/>
        <circle cx="565" cy="521" r="7"/>
        <circle cx="589" cy="499" r="7"/>
        <rect class="laptop-base" x="859" y="574" width="184" height="10" rx="5"/>
        <path class="message" d="M933 490 H969 Q972 490 972 493 V519 Q972 522 969 522 H957 L951 530 L945 522 H933 Q930 522 930 519 V493 Q930 490 933 490 Z"/>
      </g>
      <g stroke="#fca033" stroke-width="3">
        <line x1="937" y1="498" x2="965" y2="498"/>
        <line x1="937" y1="505" x2="965" y2="505"/>
        <line x1="937" y1="512" x2="955" y2="512"/>
      </g>
    </svg>

    <p class="feature-label chat" style="margin:0">Live Chat Box</p>
    <p class="feature-label stats" style="margin:0">Instant Statistics</p>
    <p class="feature-label realtime" style="margin:0">Respond in Real Time<br>from anywhere</p>
  </div>
</main>
</body>
</html>
```